Mining Engineering Services

I would like a 1 page flyer promoting RVT Mining Pty Ltd engineering services using a UAV (Unmanned aerial vehicle). I want something simple yet captures the readers attention. I have a promo video that I would like to attach a hyper link to this brochure. I have four other brochures to make after the successful completion of this one.

Target Market(s)

Mining Industry

Requirements
Must have
• Details from the word doc attached.
• Contact detail to be included;
• Dean Whitlock
• Email - dean.whitlock@rvtmining-example.com
• Phone - 0418552913

```html
<!DOCTYPE html>
<html lang="en">
<head>
<meta charset="utf-8">
<title>RVT Mining – UAV Engineering Services</title>
<link rel="stylesheet" href="https://fonts.googleapis.com/css2?family=Open+Sans:wght@400;600;700&family=Montserrat:wght@600&display=swap">
<style>
  :root {
    --navy: #1b56a4;
    --deep: #174a94;
    --sky: #27a0df;
    --sky-soft: #3cb0e8;
    --ink-blue: #1d5aa8;
    --white: #ffffff;
    --grey-text: #6b6f75;
    --earth: #7a5236;
    --earth-dark: #5b3c28;
    --pit-grey: #74716c;
    --terrain-green: #46c94a;
  }
  * { margin: 0; padding: 0; box-sizing: border-box; }
  html, body { width: 954px; height: 1200px; overflow: hidden; background: var(--white); }
  body { font-family: "Open Sans", Arial, sans-serif; color: var(--white); }
  .flyer { position: relative; width: 954px; height: 1200px; background: var(--white); overflow: hidden; }

  .brand { position: absolute; left: 260px; top: 92px; display: flex; align-items: center; gap: 16px; }
  .brand-dot { width: 46px; height: 46px; border-radius: 50%; background: var(--navy); }
  .brand-name { font-weight: 700; font-size: 44px; letter-spacing: 4px; color: var(--navy); }

  .photo { position: absolute; }
  .photo-hero { left: 0; top: 193px; width: 954px; height: 310px; background: linear-gradient(160deg, var(--earth) 0%, #8a5e3f 45%, var(--earth-dark) 100%); }
  .photo-flight { left: 741px; top: 41px; width: 180px; height: 150px; background: linear-gradient(170deg, #8d8a84 0%, var(--pit-grey) 60%, #5e5b57 100%); }
  .photo-survey { left: 741px; top: 199px; width: 180px; height: 149px; background: linear-gradient(180deg, #9fc4e6 0%, #b8ad95 45%, #6f6552 100%); }
  .photo-terrain { left: 553px; top: 356px; width: 181px; height: 147px; background: linear-gradient(150deg, #5fd85c 0%, var(--terrain-green) 55%, #35a63a 100%); border: 4px solid var(--white); }
  .photo-pit { left: 741px; top: 356px; width: 180px; height: 147px; background: linear-gradient(160deg, #8a8883 0%, #66645f 60%, #55534f 100%); border: 4px solid var(--white); }
  .photo-survey, .photo-pit { outline: 4px solid var(--white); }

  .about-tab { position: absolute; left: 0; top: 474px; width: 273px; height: 47px; }
  .about-title { position: absolute; left: 50px; top: 478px; font-size: 31px; font-weight: 700; color: var(--ink-blue); }

  .band { position: absolute; left: 0; top: 520px; width: 954px; height: 680px; background: linear-gradient(180deg, var(--navy) 0%, var(--deep) 100%); }
  .about-text { position: absolute; left: 40px; top: 549px; width: 890px; font-size: 17.4px; line-height: 24.3px; text-align: justify; }

  .services-head { position: absolute; left: 0; top: 718px; width: 431px; height: 40px; background: var(--sky); }
  .services-head h2 { font-size: 17px; font-weight: 600; padding: 8px 0 0 35px; }
  .list { list-style: none; }
  .list li { position: relative; padding-left: 20px; }
  .list li::before { content: ""; position: absolute; left: 2px; top: 0.55em; width: 6px; height: 6px; background: var(--white); }
  .services-list { position: absolute; left: 36px; top: 766px; font-size: 16.6px; line-height: 22.9px; }

  .contact { position: absolute; left: 0; top: 1077px; width: 431px; height: 123px; background: var(--white); }
  .contact-name { position: absolute; left: 44px; top: 16px; font-family: "Montserrat", Arial, sans-serif; font-weight: 600; font-size: 26px; color: var(--ink-blue); }
  .contact-rule { position: absolute; left: 44px; top: 57px; width: 305px; border-top: 2px dotted var(--ink-blue); }
  .contact-line { position: absolute; left: 44px; display: flex; align-items: center; gap: 10px; font-family: "Montserrat", Arial, sans-serif; font-size: 16.5px; color: var(--grey-text); }
  .contact-email { top: 60px; }
  .contact-phone { top: 85px; }
  .contact-line svg { width: 16px; height: 16px; fill: var(--grey-text); }

  .uav-panel { position: absolute; left: 433px; top: 701px; width: 491px; height: 499px; background: linear-gradient(180deg, var(--sky) 0%, var(--sky-soft) 100%); }
  .uav-head { position: absolute; left: 433px; top: 718px; width: 470px; height: 41px; }
  .uav-head h2 { position: absolute; left: 456px; top: 726px; font-size: 17px; font-weight: 700; color: var(--ink-blue); }
  .uav-system { position: absolute; left: 455px; top: 767px; font-size: 15.8px; font-weight: 700; }
  .uav-list { position: absolute; left: 455px; top: 792px; font-size: 15.8px; line-height: 21.4px; }
  .uav-list small { font-size: 13.5px; }
  .sensors-tab { position: absolute; left: 433px; top: 1047px; width: 208px; height: 30px; }
  .sensors-title { position: absolute; left: 455px; top: 1051px; font-size: 15.6px; font-weight: 700; }
  .sensors-list { position: absolute; left: 458px; top: 1090px; font-size: 15.8px; line-height: 21.4px; }
  .sensors-list small { font-size: 13.5px; }
</style>
</head>
<body>
<main class="flyer">
  <header class="brand">
    <span class="brand-dot"></span>
    <span class="brand-name">RVT MINING</span>
  </header>

  <div class="photo photo-hero" role="img" aria-label="Aerial photo of a fixed-wing survey drone flying over a dirt haul road with two vehicles"></div>
  <div class="photo photo-flight" role="img" aria-label="Survey drone in flight above an open pit mine"></div>
  <div class="photo photo-survey" role="img" aria-label="Drone capturing data over terraced pit benches"></div>
  <div class="photo photo-terrain" role="img" aria-label="Green digital elevation model of mine terrain"></div>
  <div class="photo photo-pit" role="img" aria-label="Aerial ortho-mosaic of a grey open pit"></div>

  <svg class="about-tab" viewBox="0 0 273 47" aria-hidden="true"><polygon points="0,0 273,0 250,47 0,47" fill="#ffffff"/></svg>
  <h1 class="about-title">About us:</h1>

  <section class="band">
  </section>
  <p class="about-text">RVT Mining Pty Ltd is a Mining Engineering consultancy company with over 15 year’s experience in the Mining industry. RVT Mining Pty Ltd provides value adding mining engineering services with the utilisation of industry leading UAV (Unmanned Aerial Vehicle) technology. RVT Mining utilises multiple sensors in the UAV to provide custom solutions to your Mine site. Unlike other UAV survey providers, RVT Mining’s engineering expertise can provide assistance from concept to reconciliation of your project.</p>

  <div class="services-head"><h2>Services include but are not limited to:</h2></div>
  <ul class="list services-list">
    <li>Mine Operation Design and Scheduling</li>
    <li>Pit Optimisation</li>
    <li>Rehabilitation Design and Planning</li>
    <li>Surface Water Drainage</li>
    <li>Open Pit/Stockpile Volumes</li>
    <li>DEM (Digital Elevation Models)</li>
    <li>Reconciliation Reporting</li>
    <li>Thermal Imaging for Volatile Materials</li>
    <li>Pit Wall Inspections</li>
    <li>Geo Referenced Ortho-Mosaics</li>
    <li>Site Rehabilitation Inspections</li>
    <li>Multispectral Imaging</li>
    <li>Surveying Services</li>
  </ul>

  <aside class="contact">
    <p class="contact-name">Dean Whitlock</p>
    <span class="contact-rule"></span>
    <p class="contact-line contact-email">
      <svg viewBox="0 0 16 16" aria-hidden="true"><rect x="1" y="4" width="14" height="10" rx="1"/><polygon points="1,4 8,9 15,4" fill="#ffffff"/></svg>
      dean.whitlock@rvtmining-example.com
    </p>
    <p class="contact-line contact-phone">
      <svg viewBox="0 0 16 16" aria-hidden="true"><path d="M4 1l3 3-2 2c1 2 3 4 5 5l2-2 3 3-2 3C7 15 1 9 1 3z"/></svg>
      (041) 855-2913
    </p>
  </aside>

  <section class="uav-panel"></section>
  <svg class="uav-head" viewBox="0 0 470 41" aria-hidden="true"><polygon points="0,0 470,0 458,41 0,41" fill="#ffffff"/></svg>
  <h2 class="uav-head-title" style="position:absolute;left:456px;top:727px;font-size:17px;font-weight:700;color:var(--ink-blue);">UAV (Unmanned Aerial Vehicle) information</h2>
  <p class="uav-system">SkyTrace S200 UAV System</p>
  <ul class="list uav-list">
    <li>1.8m Wing Span</li>
    <li>Fully Transportable</li>
    <li>Operates Under Fully Autonomous or Manual Control</li>
    <li>Highly Accurate Navigation and Positioning Systems</li>
    <li>Versatile and Flexible Operations</li>
    <li>Long Flight Time + 45min <small>(Large Surveys Per Flight)</small></li>
    <li>Able to Operate Low Rain</li>
    <li>Able to Operate in High Wind</li>
    <li>Parachute Recovery</li>
    <li>Assisted Launch</li>
    <li>Multiple Pod &amp; Sensor Capable</li>
  </ul>

  <svg class="sensors-tab" viewBox="0 0 208 30" aria-hidden="true"><polygon points="0,0 208,0 196,30 0,30" fill="#1b56a4"/></svg>
  <h3 class="sensors-title">Sensors utilised</h3>
  <ul class="list sensors-list">
    <li>RGB 24 Mega Pixel Camera <small>(Digital Elevation Models)</small></li>
    <li>Infra-red Camera (Thermal Imaging)</li>
    <li>NDVI (Multispectral Imaging)</li>
    <li>Magnetometer (Magnetic Surveys)</li>
  </ul>
</main>
</body>
</html>
```